Business Card for a Jewellery Brand

Business card for an upscale jewellery brand. Attached is the brand logo and icon and color board. I am looking for two card versions: one for the founder and one is generic. The card should be elegant and convey upscale and premium feel. I am open to both square and rectangle card shapes.

Industry/Entity Type

Jewelry

Contact Information for Business Card

Two cards: (1) Sunila Perumbadi (Founder) (2) General
(1) Sunila Perumbadi card should have Name: Sunila Perumbadi, Title: Founder Email id: sunila@quelm.com.au. Phone no: +61412555307
(2) Generic card should have Email id: info@quelm.com.au. Phone no: +61431555962

Requirements
Must have
• Workmark
• ICON
• Phone no
• Email ID
• ABN: 48917205563 (Note: ABN is Business number in Australia)
• Website: www.quelm.com.au
• Instagram: quelm_jewellery
• Facebook: @quelmjewellery
Nice to have
• Tagline

```html
<!DOCTYPE html>
<html lang="en">
<head>
<meta charset="utf-8">
<title>QUELM – Founder Card</title>
<link rel="stylesheet" href="https://fonts.googleapis.com/css2?family=Cormorant+Garamond:wght@400;500&display=swap">
<style>
  :root {
    --marble-white: #f7f7f6;
    --marble-grey: #e6e6e8;
    --marble-vein: #b3acd0;
    --brand-pink: #ee86b0;
    --ink-navy: #36335f;
  }
  * { margin: 0; padding: 0; box-sizing: border-box; }
  html, body {
    width: 667px;
    height: 1200px;
    overflow: hidden;
    background: var(--marble-white);
  }
  .card {
    position: relative;
    width: 667px;
    height: 1200px;
    overflow: hidden;
    font-family: "Cormorant Garamond", Georgia, serif;
  }
  .card__surface {
    position: absolute;
    inset: 0;
    background:
      radial-gradient(ellipse 240px 120px at 520px 660px, rgba(120,105,170,0.45), rgba(179,172,208,0) 70%),
      linear-gradient(160deg, var(--marble-white) 0%, #fbfbfa 40%, var(--marble-grey) 100%);
  }
  .brand {
    position: absolute;
    top: 158px;
    left: 0;
    width: 100%;
    display: flex;
    flex-direction: column;
    align-items: center;
  }
  .brand__dot {
    width: 96px;
    height: 96px;
    border-radius: 50%;
    background: var(--brand-pink);
    margin-top: 50px;
  }
  .brand__name {
    margin-top: 72px;
    font-size: 104px;
    line-height: 1;
    font-weight: 500;
    letter-spacing: 0.22em;
    padding-left: 0.22em;
    color: var(--brand-pink);
  }
  .contact {
    position: absolute;
    top: 800px;
    left: 0;
    width: 100%;
    text-align: center;
    color: var(--ink-navy);
    font-size: 46px;
    line-height: 58px;
    font-weight: 400;
    list-style: none;
  }
  .details {
    position: absolute;
    top: 1068px;
    left: 0;
    width: 100%;
    text-align: center;
    color: var(--ink-navy);
    font-size: 23px;
    line-height: 32px;
    font-weight: 500;
    letter-spacing: 0.02em;
    list-style: none;
  }
</style>
</head>
<body>
  <main class="card">
    <div class="card__surface" role="img" aria-label="White marble texture with a soft violet vein"></div>

    <header class="brand">
      <span class="brand__dot"></span>
      <span class="brand__name">QUELM</span>
    </header>

    <ul class="contact">
      <li class="contact__name">Sunila Perumbadi</li>
      <li class="contact__title">/Founder/</li>
      <li class="contact__email">sunila@quelm.com.au</li>
      <li class="contact__phone">+61412555307</li>
    </ul>

    <ul class="details">
      <li class="details__web">www.quelm.com.au &nbsp;·&nbsp; ABN 48917205563</li>
      <li class="details__social">Instagram quelm_jewellery &nbsp;·&nbsp; Facebook @quelmjewellery</li>
    </ul>
  </main>
</body>
</html>
```